London city running workshops

I am starting a new series of running workshops for keen city runners. I need a poster to advertise the start of the workshops which will be in London's leading running shop that I am partnering with. The poster will be displayed in A3 size in the floor to ceiling shop windows as well in in A4 size inside the shop.

My company Maple FT is relatively new, providing both one to one and group training sessions to help improve technique, fitness and educate about injury prevention through training. The company focus is on providing an excellent personal, friendly and tailored service. I am very much involved with fitness and sport specific research, ensuring I provide the latest scientific methods in a practical, applicable and effective way.

The workshops will teach you how to improve your own running technique and increase your knowledge to give you the confidence to apply the methods and run faster, easier and injury free.

Target Market(s)

central london city workers, keen runners both male and female, average 20's - 40's

Industry/Entity Type

Training

Requirements
Must have
• Slogan: Run right, run smart, run injury-free
Text: Running workshop level 1, Mondays 6.30pm, Starts January 31st
Info: Ask in store for details or book now at www.mapleft-example.com/run
Other: 'MapleFT logo' in partnership with 'Stride and Shine logo'

Feel free to challenge me on any of these if you think them unnecessary :)
Nice to have
• Perhaps a picture/photo. Something that will stand out from the other pictures associated with running shoe brands.
To convey it's not just a product but an investment in you, that will give you a real permanent improvement in your own running style.
It would be nice to have the company colours as the base for the colour palette in the poster.

```html
<!DOCTYPE html>
<html lang="en">
<head>
<meta charset="utf-8">
<title>Running Workshop Level 1 – MapleFT</title>
<link href="https://fonts.googleapis.com/css2?family=Arimo:ital,wght@0,700;1,700&display=swap" rel="stylesheet">
<style>
  :root {
    --cyan: #12a9e0;
    --cyan-light: #8fd6f2;
    --ink: #1f1f1f;
    --white: #ffffff;
    --photo-light: #eef1f5;
    --photo-mid: #c9d3de;
  }
  * { margin: 0; padding: 0; box-sizing: border-box; }
  html, body { width: 847px; height: 1200px; overflow: hidden; background: var(--white); }
  body { font-family: "Arimo", Arial, sans-serif; font-weight: 700; color: var(--ink); }
  .poster { position: relative; width: 847px; height: 1200px; }

  .slogan-band {
    position: absolute; top: 40px; left: 0; width: 847px; height: 68px;
    background: var(--cyan); color: var(--white);
    font-size: 30px; text-align: center; line-height: 68px; letter-spacing: 0.2px;
  }
  .title {
    position: absolute; top: 128px; width: 100%; text-align: center;
    font-size: 47px; letter-spacing: -0.3px;
  }
  .schedule {
    position: absolute; top: 200px; width: 100%; text-align: center;
    font-size: 35px; letter-spacing: -0.2px;
  }

  .photo {
    position: absolute; top: 268px; left: 0; width: 847px; height: 580px;
    background: radial-gradient(ellipse at 48% 55%, var(--photo-light) 0%, #dfe5ec 45%, var(--photo-mid) 100%);
  }
  .photo-edge {
    position: absolute; left: 0; width: 847px; height: 22px;
    background: linear-gradient(90deg, var(--cyan) 0%, var(--cyan-light) 45%, #e6f6fc 60%, var(--cyan) 100%);
  }
  .photo-edge.top { top: 268px; }
  .photo-edge.bottom { top: 826px; }

  .booking {
    position: absolute; top: 708px; width: 100%; text-align: center;
  }
  .booking-lead { color: var(--cyan); font-size: 38px; letter-spacing: -0.3px; }
  .booking-url { font-size: 36px; margin-top: 6px; }

  .brand-box {
    position: absolute; top: 885px; height: 105px; background: var(--cyan);
    display: flex; align-items: center; justify-content: center; gap: 12px;
    color: var(--white);
  }
  .brand-box.host { left: 35px; width: 267px; font-size: 40px; }
  .brand-box.partner { left: 576px; width: 233px; font-size: 24px; }
  .brand-mark { width: 18px; height: 18px; border-radius: 50%; background: var(--white); flex: none; }

  .partnership {
    position: absolute; top: 897px; left: 310px; width: 256px;
    text-align: center; font-size: 32px; line-height: 36px;
  }
  .investment {
    position: absolute; top: 1010px; left: 30px; width: 277px;
    text-align: center; font-size: 20px; line-height: 27px;
  }
  .contact {
    position: absolute; top: 1018px; left: 540px; width: 307px;
    text-align: center; font-size: 17px; line-height: 21px;
  }
  .contact .label { color: var(--cyan-light); }
  .contact .tel { font-size: 20px; margin-bottom: 12px; }
  .contact .block { margin-bottom: 10px; }
</style>
</head>
<body>
<div class="poster">
  <div class="slogan-band">RUN RIGHT • RUN SMART • RUN INJURY-FREE</div>
  <h1 class="title">Running Workshop Level 1</h1>
  <p class="schedule">Mondays 6.30pm - Starts January 31st</p>

  <div class="photo" role="img" aria-label="Motion-blurred photo of runners' legs and white running shoes on a road"></div>
  <div class="photo-edge top"></div>
  <div class="photo-edge bottom"></div>

  <div class="booking">
    <p class="booking-lead">Ask in store for details or book now at</p>
    <p class="booking-url">www.mapleft-example.com/run</p>
  </div>

  <div class="brand-box host"><span class="brand-mark"></span><span>MapleFT</span></div>
  <p class="partnership">in partnership<br>with</p>
  <div class="brand-box partner"><span class="brand-mark"></span><span>Stride and Shine</span></div>

  <p class="investment">offering an investment in <em>you</em>, that will give <em>you</em> a real, permanent improvement in your own running style.</p>

  <div class="contact">
    <p class="tel"><span class="label">Tel:</span> 0207 555 0142</p>
    <div class="block"><p class="label">Email:</p><p>london@strideandshine-example.com</p></div>
    <div class="block"><p class="label">Hours:</p><p>Monday-Saturday 9am-6pm</p><p>Thursday 9am-8pm</p></div>
  </div>
</div>
</body>
</html>
```